Flyer for Pharmacy/Medical Convention

Tri-fold flyer for pharmacy/medical convention. The inside of the flyer we would like to look like a venn diagram, possibly using an image similar to our blue logo

Copy write will be submitted when a design is chosen

there will be a flap about educational features, one about supplements an automated recommendations, and a flap about a computer platform to manage patients

Target Market(s)

Pharmacists and Medical Providers

Industry/Entity Type

Supplement

Colors

Designer to choose colors to be used in the design.

Requirements
Must have
• color scheme similar to logos and or label design attached

```html
<!DOCTYPE html>
<html lang="en">
<head>
<meta charset="utf-8">
<title>Veridian Therapeutic Solutions – Tri-fold Flyer</title>
<link href="https://fonts.googleapis.com/css2?family=Open+Sans:ital,wght@0,400;0,600;0,700;1,400;1,600&display=swap" rel="stylesheet">
<style>
  :root{
    --bg:#dfe3e4;
    --blue:#2b4fd6;
    --blue-deep:#1c3bbd;
    --blue-light:#6f8ff0;
    --sky:#4a8fe3;
    --ink:#3a3f4a;
    --muted:#6b7280;
    --white:#ffffff;
    --paper:#f4f5f8;
  }
  *{box-sizing:border-box;margin:0;padding:0}
  html,body{width:1200px;height:1200px;overflow:hidden;background:var(--bg);font-family:"Open Sans",Arial,sans-serif;color:var(--ink)}
  .canvas{position:relative;width:1200px;height:1200px}
  .sheet{position:absolute;left:30px;width:1140px;height:540px;display:flex;box-shadow:0 8px 24px rgba(0,0,0,.18)}
  .sheet--outside{top:30px}
  .sheet--inside{top:630px}
  .panel{position:relative;flex:0 0 380px;width:380px;height:540px;overflow:hidden;background:var(--white)}
  .panel svg.decor{position:absolute;inset:0}
  .ph{position:absolute;display:block}
  .body-text{font-size:10px;line-height:1.45;color:var(--muted)}
  .on-blue{color:var(--white)}
  .url-pill{position:absolute;height:26px;border-radius:13px;display:flex;align-items:center;justify-content:center;font-size:13px;font-weight:600;letter-spacing:.5px}
  .url-pill--blue{background:var(--blue);color:var(--white)}
  .url-pill--silver{background:linear-gradient(#f2f3f6,#c9ccd4);color:var(--blue-deep)}
  .brand{position:absolute;text-align:center;width:100%}
  .brand__name{display:inline-flex;align-items:center;gap:6px;font-size:20px;font-weight:700;color:var(--blue);letter-spacing:1px}
  .brand__dot{width:12px;height:12px;border-radius:50%;background:var(--blue)}
  .brand__tag{font-size:10px;font-weight:700;color:var(--blue-deep)}

  /* testimonial */
  .testimonial__title{position:absolute;top:28px;width:100%;text-align:center;font-size:17px;font-weight:600;letter-spacing:1.5px;color:var(--white)}
  .testimonial__list{position:absolute;top:62px;left:36px;right:30px}
  .testimonial__item{margin-bottom:10px}
  .stars{color:var(--white);font-size:12px;letter-spacing:4px}

  /* contact */
  .contact__intro{position:absolute;top:96px;left:40px;right:40px;text-align:center}
  .contact__list{position:absolute;top:322px;width:100%;text-align:center}
  .contact__item{margin-bottom:16px;font-size:12px;font-weight:600;color:var(--ink);letter-spacing:.3px}
  .contact__item svg{display:block;margin:0 auto 6px}

  /* cover */
  .cover__heading{position:absolute;top:330px;width:100%;text-align:center;color:var(--white)}
  .cover__title{font-size:34px;font-weight:600;letter-spacing:3px}
  .cover__sub{font-size:18px;font-weight:600;letter-spacing:2px;margin-top:2px}
  .cover__lead{font-size:12px;margin:10px 40px 0;line-height:1.4}

  /* inside */
  .section-title{font-size:20px;font-style:italic;font-weight:600;color:var(--sky);line-height:1.05}
  .about__content{position:absolute;top:26px;left:32px;right:30px}
  .about__content .body-text{margin-top:8px}
  .convention__content{position:absolute;top:26px;left:28px;right:28px}
  .convention__content .body-text{margin-top:8px}
  .convention__lead{margin-top:8px;font-size:11px;font-weight:700;font-style:italic;color:var(--sky)}
  .bullets{display:flex;gap:30px;margin-top:8px}
  .bullets ul{list-style:none;font-size:10px;color:var(--muted)}
  .bullets li{margin-bottom:2px}
  .bullets li::before{content:"★";color:var(--sky);margin-right:8px}

  .research__title{position:absolute;top:28px;width:100%;text-align:center;font-size:18px;font-weight:600;letter-spacing:2px;color:var(--white)}
  .research__item{position:absolute;left:30px;right:30px;text-align:center;color:var(--white)}
  .research__item .ph{position:relative;margin:0 auto 6px;width:74px;height:74px;border-radius:50%;border:3px solid var(--white)}
  .research__name{font-size:14px;font-weight:600}
  .research__text{font-size:10px;line-height:1.4}
</style>
</head>
<body>
<div class="canvas">

  <!-- Outside -->
  <section class="sheet sheet--outside">
    <div class="panel testimonial">
      <svg class="decor" width="380" height="540" viewBox="0 0 380 540">
        <defs>
          <linearGradient id="tBlue" x1="0" y1="0" x2="1" y2="1">
            <stop offset="0" stop-color="#2a4bd4"/><stop offset="1" stop-color="#7b98f0"/>
          </linearGradient>
        </defs>
        <rect width="380" height="540" fill="url(#tBlue)"/>
      </svg>
      <svg class="ph" role="img" aria-label="Photo of an open hand holding red and white capsules" style="left:0;top:0" width="380" height="540" viewBox="0 0 380 540">
        <defs>
          <linearGradient id="pills" x1="0" y1="0" x2="1" y2="1">
            <stop offset="0" stop-color="#d8c6a6"/><stop offset=".6" stop-color="#c89a80"/><stop offset="1" stop-color="#b64a5e"/>
          </linearGradient>
        </defs>
        <path d="M0,300 Q150,230 380,250 L380,540 L0,540 Z" fill="url(#pills)"/>
        <path d="M0,300 Q150,230 380,250" fill="none" stroke="#ffffff" stroke-width="5"/>
      </svg>
      <h2 class="testimonial__title">TESTIMONIAL</h2>
      <div class="testimonial__list">
        <div class="testimonial__item"><div class="stars">★★★★★</div><p class="body-text on-blue">Lorem Ipsum is simply dummy text of the printing and typesetting industry. Lorem Ipsum has been the industry's standard dummy text ever since the 1500s, when an unknown printer took a galley.</p></div>
        <div class="testimonial__item"><div class="stars">★★★★★</div><p class="body-text on-blue">Lorem Ipsum is simply dummy text of the printing and typesetting industry. Lorem Ipsum has been the industry's standard dummy text ever since the 1500s, when an unknown printer took a galley.</p></div>
        <div class="testimonial__item"><div class="stars">★★★★★</div><p class="body-text on-blue">Lorem Ipsum is simply dummy text of the printing and typesetting industry.</p></div>
      </div>
    </div>

    <div class="panel contact">
      <div class="brand" style="top:34px"><span class="brand__name"><span class="brand__dot"></span>VERIDIAN</span><div class="brand__tag">Therapeutic Solutions</div></div>
      <p class="body-text contact__intro">Lorem Ipsum is simply dummy text of the printing and typesetting industry. Lorem Ipsum has been the industry's standard dummy text ever since the 1500s, when an unknown printer took a galley of type and scrambled it to make a type specimen book. It has survived not only five centuries, but also the leap into electronic typesetting, remaining essentially unchanged.</p>
      <svg class="ph" role="img" aria-label="Street map showing the venue location" style="left:130px;top:222px" width="120" height="90" viewBox="0 0 120 90">
        <ellipse cx="60" cy="45" rx="58" ry="43" fill="#eef0f4" stroke="#d3d7de"/>
      </svg>
      <div class="contact__list">
        <div class="contact__item">
          <svg width="14" height="18" viewBox="0 0 14 18"><path d="M7 0a7 7 0 0 0-7 7c0 5 7 11 7 11s7-6 7-11a7 7 0 0 0-7-7zm0 10a3 3 0 1 1 0-6 3 3 0 0 1 0 6z" fill="#2b4fd6"/></svg>
          Dummy City, Dummy Country, Land
        </div>
        <div class="contact__item">
          <svg width="22" height="14" viewBox="0 0 22 14"><rect width="22" height="14" fill="#2b4fd6"/><path d="M0 0l11 8 11-8" fill="none" stroke="#fff" stroke-width="1.5"/></svg>
          info@veridiantherapeutic.com
        </div>
        <div class="contact__item">
          <svg width="20" height="16" viewBox="0 0 20 16"><path d="M1 5c0-3 4-4 9-4s9 1 9 4l-4 1-1-2H6L5 6zM5 7h10l3 8H2z" fill="#2b4fd6"/><circle cx="10" cy="11" r="2.5" fill="#fff"/></svg>
          000.0000.0000
        </div>
      </div>
      <div class="url-pill url-pill--blue" style="left:30px;right:30px;bottom:22px">www.veridiantherapeutic.com</div>
    </div>

    <div class="panel cover">
      <svg class="decor" width="380" height="540" viewBox="0 0 380 540">
        <defs>
          <linearGradient id="cBlue" x1="0" y1="0" x2="1" y2="1">
            <stop offset="0" stop-color="#2644cf"/><stop offset="1" stop-color="#5c7de8"/>
          </linearGradient>
        </defs>
        <rect width="380" height="540" fill="url(#cBlue)"/>
        <path d="M0,0 H380 V250 Q300,330 190,320 Q80,310 0,240 Z" fill="#ffffff"/>
      </svg>
      <div class="brand" style="top:22px"><span class="brand__name"><span class="brand__dot"></span>VERIDIAN</span><div class="brand__tag">Therapeutic Solutions</div></div>
      <svg class="ph" role="img" aria-label="Photo of two clinicians in coats reviewing a tablet" style="left:30px;top:70px" width="320" height="240" viewBox="0 0 320 240">
        <defs>
          <linearGradient id="docs" x1="0" y1="0" x2="1" y2="1">
            <stop offset="0" stop-color="#e9eef6"/><stop offset="1" stop-color="#4a9be6"/>
          </linearGradient>
        </defs>
        <path d="M0,0 H320 V150 Q240,240 160,236 Q70,232 0,150 Z" fill="url(#docs)"/>
        <path d="M0,150 Q70,232 160,236 Q240,240 320,150" fill="none" stroke="#c9ccd4" stroke-width="6"/>
      </svg>
      <div class="cover__heading">
        <div class="cover__title">YOUR HEADING</div>
        <div class="cover__sub">YOUR SUB - HEADING</div>
        <p class="cover__lead">Lorem Ipsum is simply dummy text of the printing and type setting industry</p>
      </div>
      <div class="url-pill url-pill--silver" style="left:26px;right:26px;bottom:34px;height:32px;border-radius:16px;font-size:15px">www.veridiantherapeutic.com</div>
    </div>
  </section>

  <!-- Inside -->
  <section class="sheet sheet--inside">
    <div class="panel about">
      <svg class="decor" width="380" height="540" viewBox="0 0 380 540">
        <rect width="380" height="540" fill="var(--paper)"/>
        <path d="M0,520 Q200,525 380,470 L380,540 L0,540 Z" fill="#2b4fd6"/>
      </svg>
      <div class="about__content">
        <h2 class="section-title">About Us</h2>
        <p class="body-text">Lorem Ipsum is simply dummy text of the printing and typesetting industry. Lorem Ipsum has been the industry's standard dummy text ever since the 1500s, when an unknown printer took a galley of type and scrambled it to make a type specimen book. It has survived not only five centuries, but also the leap into electronic typesetting, remaining essentially unchanged.</p>
        <p class="body-text">Lorem Ipsum is simply dummy text of the printing and typesetting industry. Lorem Ipsum has been the industry's standard dummy text ever since the 1500s, when an unknown printer took a galley of type and scrambled it to make a type specimen book. It has survived not only five centuries, but also the leap into electronic typesetting, remaining essentially unchanged.</p>
      </div>
      <svg class="ph" role="img" aria-label="Hand-lettered diagram of overlapping circles around Healthy Life: exercise regularly, eat healthy, reduce stress, drink plenty of water, with a pointing hand" style="left:20px;top:290px" width="340" height="210" viewBox="0 0 340 210">
        <defs>
          <radialGradient id="venn" cx=".5" cy=".45" r=".6">
            <stop offset="0" stop-color="#f6f3e2"/><stop offset="1" stop-color="#e6e9f0"/>
          </radialGradient>
        </defs>
        <rect width="340" height="210" rx="10" fill="url(#venn)"/>
      </svg>
    </div>

    <div class="panel convention">
      <svg class="decor" width="380" height="540" viewBox="0 0 380 540">
        <defs>
          <linearGradient id="vBlue" x1="0" y1="1" x2="1" y2="0">
            <stop offset="0" stop-color="#2a48d2"/><stop offset="1" stop-color="#8aa3f2"/>
          </linearGradient>
        </defs>
        <rect width="380" height="540" fill="#ffffff"/>
        <path d="M0,540 V420 Q240,400 380,230 V540 Z" fill="url(#vBlue)"/>
      </svg>
      <div class="convention__content">
        <h2 class="section-title">Pharmacy<br>Medical Convention</h2>
        <p class="body-text">Lorem Ipsum is simply dummy text of the printing and typesetting industry. Lorem Ipsum has been the industry's standard dummy text ever since the 1500s, when an unknown printer took a galley.</p>
        <p class="body-text">Lorem Ipsum is simply dummy text of the printing and typesetting industry. Lorem Ipsum has been the industry's standard dummy text ever since the 1500s, when an unknown printer took a galley.</p>
        <p class="convention__lead">Lorem Ipsum is simply dummy text</p>
        <div class="bullets">
          <ul><li>Lorem Ipsum</li><li>Lorem Ipsum</li><li>Lorem Ipsum</li><li>Lorem Ipsum</li><li>Lorem Ipsum</li><li>Lorem Ipsum</li></ul>
          <ul><li>Lorem Ipsum</li><li>Lorem Ipsum</li><li>Lorem Ipsum</li><li>Lorem Ipsum</li></ul>
        </div>
      </div>
      <svg class="ph" role="img" aria-label="Photo of a lab researcher looking into a microscope" style="left:110px;top:328px" width="166" height="166" viewBox="0 0 166 166">
        <defs>
          <linearGradient id="lab" x1="0" y1="0" x2="1" y2="1">
            <stop offset="0" stop-color="#f1f3f6"/><stop offset="1" stop-color="#9aa6b8"/>
          </linearGradient>
        </defs>
        <circle cx="83" cy="83" r="78" fill="url(#lab)" stroke="#d7dae1" stroke-width="7"/>
      </svg>
      <div class="url-pill url-pill--silver" style="left:60px;right:40px;bottom:14px;height:22px;font-size:11px">www.veridiantherapeutic.com</div>
    </div>

    <div class="panel research">
      <svg class="decor" width="380" height="540" viewBox="0 0 380 540">
        <defs>
          <linearGradient id="rBlue" x1="0" y1="0" x2="0" y2="1">
            <stop offset="0" stop-color="#2645d0"/><stop offset=".6" stop-color="#4f72e6"/><stop offset="1" stop-color="#2d4ed6"/>
          </linearGradient>
        </defs>
        <rect width="380" height="540" fill="url(#rBlue)"/>
      </svg>
      <h2 class="research__title">MEDICAL RESEACH</h2>
      <div class="research__item" style="top:72px">
        <span class="ph" role="img" aria-label="Photo of white supplement capsules on green leaves" style="background:radial-gradient(#f4f7f0,#5fae4e)"></span>
        <div class="research__name">Lorem Ipsum</div>
        <p class="research__text">Lorem Ipsum is simply dummy text of the printing and typesetting industry. Lorem Ipsum has been the industry's standard dummy text.</p>
      </div>
      <div class="research__item" style="top:225px">
        <span class="ph" role="img" aria-label="Photo of medical instruments in blue light" style="background:radial-gradient(#e6f4f8,#66b6cf)"></span>
        <div class="research__name">Lorem Ipsum</div>
        <p class="research__text">Lorem Ipsum is simply dummy text of the printing and typesetting industry. Lorem Ipsum has been the industry's standard dummy text.</p>
      </div>
      <div class="research__item" style="top:380px">
        <span class="ph" role="img" aria-label="Photo of a blood pressure monitor and pill organiser" style="background:radial-gradient(#f3f5f8,#8fa7c4)"></span>
        <div class="research__name">Lorem Ipsum</div>
        <p class="research__text">Lorem Ipsum is simply dummy text of the printing and typesetting industry. Lorem Ipsum has been the industry's standard dummy text.</p>
      </div>
    </div>
  </section>

</div>
</body>
</html>
```